Communications Contractor Business Card Design

I would like a new business card for a new Communications company in Australia. Subcontracting and specialising in cabling, data, phone, antennas, pay tv ,modems, audio visual fibre optics etc. I am open to colour and design concepts but would like a modern clean look that stands out.

Industry/Entity Type

Tv

Contact Information for Business Card

kestrel communications pty ltd, Doug Pemberton, PO BOX 657 Marlow Flats QLD 4873 kestrel4me@maildrop-example.com Australia. ph 0437196084. Director/Technician. services- Cabling,data,phone,antennas,audio visual,home theatre, fibre optics.

```html
<!DOCTYPE html>
<html lang="en">
<head>
<meta charset="utf-8">
<title>Kestrel Communications – Business Card</title>
<link href="https://fonts.googleapis.com/css2?family=Ubuntu:wght@400;500&display=swap" rel="stylesheet">
<style>
  :root {
    --page: #e6e2d6;
    --sky: #57afd4;
    --sky-light: #5dbde4;
    --navy: #1e5067;
    --teal: #2c7390;
    --steel: #3a87a6;
    --shield: #eaf2f5;
    --pale-text: #b4e0f2;
    --white: #ffffff;
  }
  * { box-sizing: border-box; margin: 0; padding: 0; }
  html, body { width: 1200px; height: 834px; overflow: hidden; }
  body {
    background: var(--page);
    font-family: "Ubuntu", sans-serif;
    display: flex;
    flex-direction: column;
    align-items: center;
    justify-content: center;
    gap: 40px;
  }
  .card {
    position: relative;
    width: 600px;
    height: 365px;
    overflow: hidden;
    box-shadow: 0 4px 14px rgba(0,0,0,0.18);
  }
  /* Front */
  .card--front { background: var(--sky); }
  .card--front .facets { position: absolute; inset: 0; }
  .website {
    position: absolute;
    top: 160px;
    left: 0;
    width: 100%;
    text-align: center;
    font-size: 30px;
    font-weight: 500;
    color: var(--pale-text);
    letter-spacing: 0.5px;
  }
  .website .domain { color: var(--navy); }
  /* Back */
  .card--back { background: var(--navy); color: var(--white); }
  .company {
    height: 73px;
    display: flex;
    align-items: center;
    justify-content: center;
    font-size: 22px;
    font-weight: 500;
    background: var(--navy);
  }
  .row {
    position: relative;
    height: 73px;
    display: flex;
    align-items: center;
    padding-left: 125px;
    font-size: 17px;
    line-height: 1.3;
  }
  .row--address { background: var(--sky); }
  .row--email { background: var(--teal); }
  .row--phone { background: var(--steel); }
  .row--services { background: var(--navy); }
  .row .shield {
    position: absolute;
    left: 49px;
    top: 0;
    width: 64px;
    height: 66px;
  }
</style>
</head>
<body>

  <section class="card card--front">
    <svg class="facets" viewBox="0 0 600 365" aria-hidden="true">
      <polygon points="0,0 150,0 0,205" fill="var(--sky-light)"/>
      <polygon points="600,105 600,260 520,220 530,130" fill="var(--navy)"/>
      <polygon points="600,300 600,365 470,365" fill="var(--teal)"/>
    </svg>
    <p class="website">www.<span class="domain">kestrelcomms</span>.example</p>
  </section>

  <section class="card card--back">
    <h1 class="company">kestrel communications pty ltd</h1>

    <div class="row row--address">
      <svg class="shield" viewBox="0 0 64 66" aria-hidden="true">
        <polygon points="0,0 64,0 64,46 32,66 0,46" fill="var(--shield)"/>
        <path d="M32 14 L20 25 H24 V36 H30 V29 H34 V36 H40 V25 H44 Z" fill="var(--navy)"/>
      </svg>
      <p>Doug Pemberton, PO BOX 657 Marlow Flats QLD 4873</p>
    </div>

    <div class="row row--email">
      <svg class="shield" viewBox="0 0 64 66" aria-hidden="true">
        <polygon points="0,0 64,0 64,46 32,66 0,46" fill="var(--shield)"/>
        <rect x="17" y="17" width="30" height="20" fill="none" stroke="var(--navy)" stroke-width="2.5"/>
        <path d="M17 17 L32 29 L47 17 M17 37 L28 27 M47 37 L36 27" fill="none" stroke="var(--navy)" stroke-width="2"/>
      </svg>
      <p>kestrel4me@maildrop-example.com</p>
    </div>

    <div class="row row--phone">
      <svg class="shield" viewBox="0 0 64 66" aria-hidden="true">
        <polygon points="0,0 64,0 64,46 32,66 0,46" fill="var(--shield)"/>
        <path d="M40 13 L46 18 L42 22 L38 19 C33 23 29 29 27 35 L31 37 L29 42 L22 40 C22 30 30 18 40 13 Z" fill="var(--navy)"/>
      </svg>
      <p>0437196084.</p>
    </div>

    <div class="row row--services">
      <svg class="shield" viewBox="0 0 64 66" aria-hidden="true">
        <polygon points="0,0 64,0 64,46 32,66 0,46" fill="var(--shield)"/>
        <circle cx="32" cy="27" r="12" fill="none" stroke="var(--navy)" stroke-width="5" stroke-dasharray="4.7 4.7"/>
        <circle cx="32" cy="27" r="10" fill="var(--navy)"/>
        <circle cx="32" cy="27" r="4" fill="var(--shield)"/>
      </svg>
      <p>Director/Technician. services- Cabling,data,phone,<br>antennas,audio visual,home theatre, fibre optics</p>
    </div>
  </section>

</body>
</html>
```